Home Inspection Company - Business Cards, Letterhead and Email Signature
Keystone Survey, LLC
Home Inspection Company - Business Cards, Letterhead and Email Signature - Real Estate
Creative Brief
Use same font as used in my logo
Helvetica
Professional
Dennis Larkhaven, LPR
Owner/Inspector
718 Brambleton Ct, Menlo Park, CA 94031
info@keystonesurvey-example.net
www.keystonesurvey-example.net
NQVB Certified Inspector #583019
I am looking for a clean, professional look on the business card, letterhead and email signature that compliments the "industrial/garage" look of the recently redesigned logo. Color Used: #4d4e52 Font used Helvetica (black condensed) for Keystone text Helvetica (bold ) for Inspection text Please also include the NQVB Logo.
Keystone Keystone
The NQVB logo should be below my Name and Title.
The NQVB logo should be below myName and Title.

```html
<!DOCTYPE html>
<html lang="en">
<head>
<meta charset="utf-8">
<title>Keystone Survey, LLC – Stationery Set</title>
<link rel="stylesheet" href="https://fonts.googleapis.com/css2?family=Archivo:wght@400;700;900&display=swap">
<style>
  :root {
    --brand: #4d4e52;
    --brand-dark: #3f4044;
    --paper: #ffffff;
    --backdrop: #c6c6c6;
    --ink-soft: #8a8b8e;
    --ghost: #ececec;
  }
  * { box-sizing: border-box; margin: 0; padding: 0; }
  html, body { width: 1200px; height: 415px; overflow: hidden; }
  body {
    background: var(--backdrop);
    font-family: "Archivo", Helvetica, Arial, sans-serif;
    color: var(--brand);
    position: relative;
  }
  .piece { position: absolute; background: var(--paper); overflow: hidden; }

  /* brand lockup: plain circle + name */
  .brand { display: flex; align-items: center; gap: 4px; font-weight: 900; text-transform: uppercase; letter-spacing: .02em; line-height: 1; white-space: nowrap; }
  .brand .dot { border-radius: 50%; background: currentColor; flex: none; }
  .brand--xs { font-size: 6px; } .brand--xs .dot { width: 6px; height: 6px; }
  .brand--sm { font-size: 9px; } .brand--sm .dot { width: 9px; height: 9px; }
  .brand--md { font-size: 13px; } .brand--md .dot { width: 13px; height: 13px; }
  .brand--lg { font-size: 20px; gap: 6px; } .brand--lg .dot { width: 20px; height: 20px; }
  .brand--light { color: var(--paper); }

  .ghost-mark { position: absolute; border-radius: 50%; border: 10px solid var(--ghost); }

  .small-print { font-size: 3.4px; line-height: 1.5; color: var(--ink-soft); font-weight: 400; }

  /* folder */
  .folder-cover { left: 12px; top: 29px; width: 228px; height: 367px; background: var(--brand); }
  .folder-inside { left: 240px; top: 29px; width: 230px; height: 367px; }
  .folder-cover .brand--lg { position: absolute; left: 62px; top: 70px; }
  .folder-pocket { position: absolute; left: 0; bottom: 0; width: 100%; height: 120px; background: var(--brand-dark); }
  .folder-pocket .brand { position: absolute; left: 86px; top: 34px; transform: rotate(180deg); }
  .folder-cover .ghost-mark { left: 60px; top: 150px; width: 110px; height: 110px; border-color: rgba(255,255,255,.06); }
  .folder-inside .ghost-mark { left: 40px; top: 150px; width: 140px; height: 140px; }

  /* letterheads */
  .letterhead .brand { position: absolute; left: 10px; top: 12px; }
  .letterhead .ghost-mark { right: -18px; bottom: 24px; }
  .letterhead .small-print { position: absolute; left: 10px; bottom: 8px; }

  .lh-small { left: 492px; top: 31px; width: 108px; height: 101px; }
  .lh-small .ghost-mark { width: 56px; height: 56px; border-width: 7px; }
  .lh-tall { left: 708px; top: 19px; width: 84px; height: 113px; }
  .lh-tall .ghost-mark { width: 56px; height: 56px; border-width: 7px; }
  .lh-1 { left: 492px; top: 151px; width: 156px; height: 209px; }
  .lh-2 { left: 672px; top: 151px; width: 156px; height: 209px; }
  .lh-1 .ghost-mark, .lh-2 .ghost-mark { width: 110px; height: 110px; }
  .comp-slip { left: 852px; top: 151px; width: 156px; height: 89px; }
  .comp-slip .ghost-mark { width: 60px; height: 60px; border-width: 7px; bottom: 6px; }

  /* disc */
  .disc { position: absolute; left: 613px; top: 36px; width: 84px; height: 84px; }

  /* business cards */
  .card { width: 139px; height: 48px; padding: 7px 9px; }
  .card-front { left: 809px; top: 31px; display: flex; align-items: center; justify-content: center; }
  .card-back { left: 809px; top: 89px; }
  .card-back-2 { left: 960px; top: 31px; width: 108px; }
  .card-dark { left: 960px; top: 89px; width: 108px; background: var(--brand); display: flex; align-items: center; justify-content: center; }
  .card-name { font-size: 5.5px; font-weight: 700; color: var(--brand); }
  .card-title { font-size: 3.8px; color: var(--ink-soft); margin-bottom: 3px; }
  .badge { position: absolute; right: 9px; top: 8px; width: 12px; height: 12px; border-radius: 50%; background: var(--ghost); }

  /* envelope */
  .envelope { left: 859px; top: 252px; width: 209px; height: 108px; }
  .envelope svg { position: absolute; inset: 0; }
  .envelope .brand { position: absolute; left: 50%; top: 66px; transform: translateX(-50%); }

  /* email signature screens */
  .screen { border: 1px solid #d8d8d8; padding: 8px 6px; }
  .screen-phone { left: 1085px; top: 149px; width: 38px; height: 91px; }
  .screen-tablet { left: 1092px; top: 240px; width: 96px; height: 140px; padding: 12px 10px; }
  .screen .rule { height: 1px; background: var(--ghost); margin: 5px 0; }
</style>
</head>
<body>

  <section class="piece folder-cover">
    <div class="brand brand--lg brand--light"><span class="dot"></span>Keystone</div>
    <div class="ghost-mark"></div>
    <div class="folder-pocket">
      <div class="brand brand--sm brand--light"><span class="dot"></span>Keystone</div>
    </div>
  </section>
  <section class="piece folder-inside">
    <div class="ghost-mark"></div>
  </section>

  <article class="piece letterhead lh-small">
    <div class="brand brand--xs"><span class="dot"></span>Keystone</div>
    <div class="ghost-mark"></div>
  </article>

  <svg class="disc" viewBox="0 0 84 84" aria-hidden="true">
    <circle cx="42" cy="42" r="41" fill="#4d4e52"/>
    <circle cx="42" cy="42" r="10" fill="#c6c6c6"/>
    <circle cx="42" cy="42" r="5" fill="#ffffff"/>
  </svg>

  <article class="piece letterhead lh-tall">
    <div class="brand brand--xs"><span class="dot"></span>Keystone</div>
    <div class="ghost-mark"></div>
  </article>

  <div class="piece card card-front">
    <div class="brand brand--sm"><span class="dot"></span>Keystone</div>
  </div>
  <div class="piece card card-back">
    <p class="card-name">Dennis Larkhaven, LPR</p>
    <p class="card-title">Owner/Inspector</p>
    <p class="small-print">718 Brambleton Ct, Menlo Park, CA 94031<br>info@keystonesurvey-example.net<br>www.keystonesurvey-example.net</p>
    <span class="badge"></span>
  </div>
  <div class="piece card card-back-2">
    <p class="card-name">Dennis Larkhaven, LPR</p>
    <p class="card-title">Owner/Inspector</p>
    <p class="small-print">NQVB Certified Inspector #583019<br>info@keystonesurvey-example.net</p>
  </div>
  <div class="piece card card-dark">
    <div class="brand brand--sm brand--light"><span class="dot"></span>Keystone</div>
  </div>

  <article class="piece letterhead lh-1">
    <div class="brand brand--sm"><span class="dot"></span>Keystone</div>
    <div class="ghost-mark"></div>
    <p class="small-print">718 Brambleton Ct, Menlo Park, CA 94031 · www.keystonesurvey-example.net</p>
  </article>
  <article class="piece letterhead lh-2">
    <div class="brand brand--sm"><span class="dot"></span>Keystone</div>
    <div class="ghost-mark"></div>
    <p class="small-print">718 Brambleton Ct, Menlo Park, CA 94031 · www.keystonesurvey-example.net</p>
  </article>
  <article class="piece letterhead comp-slip">
    <div class="brand brand--sm"><span class="dot"></span>Keystone</div>
    <div class="ghost-mark"></div>
    <p class="small-print">info@keystonesurvey-example.net</p>
  </article>

  <div class="piece envelope">
    <svg viewBox="0 0 209 108" preserveAspectRatio="none" aria-hidden="true">
      <polygon points="0,0 209,0 104.5,52" fill="#4d4e52"/>
    </svg>
    <div class="brand brand--xs"><span class="dot"></span>Keystone</div>
  </div>

  <div class="piece screen screen-phone">
    <div class="brand brand--xs"><span class="dot"></span>Keystone</div>
    <div class="rule"></div>
    <p class="small-print">Dennis Larkhaven<br>Owner/Inspector</p>
  </div>
  <div class="piece screen screen-tablet">
    <div class="brand brand--sm"><span class="dot"></span>Keystone</div>
    <div class="rule"></div>
    <p class="card-name">Dennis Larkhaven, LPR</p>
    <p class="card-title">Owner/Inspector</p>
    <p class="small-print">info@keystonesurvey-example.net<br>www.keystonesurvey-example.net</p>
  </div>

</body>
</html>
```